Brightmere Business Card Redesign & Logo Update

We need to update our business cards to something more modern and fresh. Brightmere can provide the current color schemes and old design examples, but welcome creativity in helping us with this redesign. PLEASE NOTE that we no longer utilize the "tree" and/or "leaf" imagery in our branding. If able would apprecaite an update on the quality of our "words only" logo in Ai. / PNG formats too.

Target Market(s)

Investors, landowners, corporate partners, contractors

Industry/Entity Type

Environmental Restoration & Conservation

Contact Information for Business Card

Logo, persons name, title, mailing address, phone and email, website url

Font styles to use
Other font styles liked:
• Merriweather

Requirements
Nice to have
• Logo, persons name, title, mailing address, phone and email, website url, but open to ideams
Should not have
• No all back backgrounds

```html
<!DOCTYPE html>
<html lang="en">
<head>
<meta charset="utf-8">
<title>Brightmere Business Card</title>
<link rel="stylesheet" href="https://fonts.googleapis.com/css2?family=Montserrat:wght@400;500;600&display=swap">
<style>
  :root {
    --green: #02531f;
    --green-deep: #014418;
    --orange: #f08a1c;
    --white: #ffffff;
    --backdrop: #3a3a3a;
  }
  * { box-sizing: border-box; margin: 0; padding: 0; }
  html, body { width: 1200px; height: 1200px; overflow: hidden; }
  body {
    background: var(--backdrop);
    display: flex;
    flex-direction: column;
    align-items: center;
    justify-content: center;
    gap: 70px;
    font-family: "Montserrat", sans-serif;
  }
  .card {
    position: relative;
    width: 760px;
    height: 434px;
    border-radius: 30px;
    overflow: hidden;
    box-shadow: 0 10px 30px rgba(0,0,0,0.45);
  }

  /* Front */
  .card--front { background: var(--white); }
  .front__top {
    position: absolute; left: 0; top: 0; width: 100%; height: 232px;
    display: flex; align-items: center; justify-content: center;
  }
  .front__stripe {
    position: absolute; left: 0; top: 232px; width: 100%; height: 8px;
    background: var(--orange);
  }
  .front__bottom {
    position: absolute; left: 0; top: 240px; width: 100%; bottom: 0;
    background: var(--green);
  }
  .wordmark {
    font-family: "Montserrat", sans-serif;
    font-weight: 600;
    line-height: 1;
    letter-spacing: 2px;
  }
  .wordmark--front { font-size: 72px; color: var(--green); }
  .wordmark--back { font-size: 92px; color: var(--white); margin-top: -30px; }

  .person {
    position: absolute; left: 56px; top: 82px;
    padding-left: 18px;
    border-left: 4px solid var(--orange);
  }
  .person__name { color: var(--orange); font-size: 30px; font-weight: 500; letter-spacing: 1px; line-height: 1.1; }
  .person__title { color: var(--white); font-size: 13px; letter-spacing: 1px; margin-top: 2px; }

  .divider {
    position: absolute; left: 380px; top: 24px; width: 1px; height: 150px;
    background: rgba(255,255,255,0.35);
  }
  .contact {
    position: absolute; left: 420px; top: 28px;
    list-style: none;
    font-size: 15px; color: var(--white);
  }
  .contact__item { display: flex; align-items: flex-start; gap: 10px; margin-bottom: 9px; line-height: 1.2; }
  .contact__icon { width: 16px; height: 16px; flex: none; margin-top: 1px; }

  /* Back */
  .card--back {
    background: linear-gradient(100deg, var(--green-deep) 0%, var(--green) 45%, #0f6a33 55%, var(--green) 70%, var(--green-deep) 100%);
    display: flex; align-items: center; justify-content: center;
  }
  .back__band {
    position: absolute; left: 300px; bottom: 22px; width: 380px; height: 16px;
    background: var(--orange);
  }
</style>
</head>
<body>
  <section class="card card--front">
    <div class="front__top">
      <span class="wordmark wordmark--front">Brightmere</span>
    </div>
    <div class="front__stripe"></div>
    <div class="front__bottom">
      <div class="person">
        <p class="person__name">JOHN DOE</p>
        <p class="person__title">POSITION</p>
      </div>
      <div class="divider"></div>
      <ul class="contact">
        <li class="contact__item">
          <svg class="contact__icon" viewBox="0 0 24 24"><path fill="#f08a1c" d="M6.6 10.8a15 15 0 0 0 6.6 6.6l2.2-2.2a1 1 0 0 1 1-.25 11.4 11.4 0 0 0 3.6.57 1 1 0 0 1 1 1V20a1 1 0 0 1-1 1A17 17 0 0 1 3 4a1 1 0 0 1 1-1h3.5a1 1 0 0 1 1 1c0 1.25.2 2.45.57 3.57a1 1 0 0 1-.25 1z"/></svg>
          <span>(000) 000 0000</span>
        </li>
        <li class="contact__item">
          <svg class="contact__icon" viewBox="0 0 24 24"><rect x="2" y="5" width="20" height="14" rx="1" fill="#f08a1c"/><path d="M2 6l10 7 10-7" fill="none" stroke="#02531f" stroke-width="2"/></svg>
          <span>email@youremail.com</span>
        </li>
        <li class="contact__item">
          <svg class="contact__icon" viewBox="0 0 24 24" fill="none" stroke="#f08a1c" stroke-width="2"><circle cx="12" cy="12" r="10"/><path d="M2 12h20M12 2c3 3 3 17 0 20M12 2c-3 3-3 17 0 20"/></svg>
          <span>www.yourwebsite.com</span>
        </li>
        <li class="contact__item">
          <svg class="contact__icon" viewBox="0 0 24 24"><path fill="#f08a1c" d="M12 2a7 7 0 0 0-7 7c0 5 7 13 7 13s7-8 7-13a7 7 0 0 0-7-7zm0 9.5A2.5 2.5 0 1 1 12 6.5a2.5 2.5 0 0 1 0 5z"/></svg>
          <span>123 Name Street, 000<br>Your City, 00000-000</span>
        </li>
      </ul>
    </div>
  </section>

  <section class="card card--back">
    <span class="wordmark wordmark--back">Brightmere</span>
    <div class="back__band"></div>
  </section>
</body>
</html>
```